dun card

personal description --- I will use this card to introduce myself to other physicians

This is only a one sided card. Primarily it would contain my picture, my clinic logo, my bio, and my clinic contact info

Target Market(s)

only to other physicians

Requirements
Must have
• ---my contact info for both office locations
• --- a sentence at the bottom of the card " I appreciate the opportunity to serve you and your patients"

```html
<!DOCTYPE html>
<html lang="en">
<head>
<meta charset="utf-8">
<title>Dun Harlow, M.D. — Introduction Card</title>
<link href="https://fonts.googleapis.com/css2?family=Crimson+Text:wght@400;600&family=Open+Sans:wght@400;600&display=swap" rel="stylesheet">
<style>
  :root {
    --page: #dcd9d4;
    --magenta: #9c2a6f;
    --slate: #50545b;
    --paper: #e7e7e7;
    --ink: #686868;
    --white: #ffffff;
    --serif: "Crimson Text", Georgia, serif;
    --sans: "Open Sans", Arial, sans-serif;
  }
  * { box-sizing: border-box; margin: 0; padding: 0; }
  html, body { width: 1200px; height: 2214px; overflow: hidden; }
  body { background: var(--page); }

  .card {
    position: absolute; left: 120px; top: 62px;
    width: 960px; height: 2089px;
    display: flex; flex-direction: column;
    background: var(--paper);
  }

  .site-bar {
    height: 111px; flex: none; background: var(--magenta);
    display: flex; align-items: center; justify-content: center;
    font-family: var(--serif); color: var(--white);
    font-size: 40px; letter-spacing: 1px;
  }

  .hero { position: relative; height: 560px; flex: none; }
  .hero-backdrop {
    position: absolute; inset: 0;
    background: linear-gradient(90deg, #dfe2e6 0%, #f3f4f6 55%, #f7f7f8 100%);
  }
  .portrait {
    position: absolute; left: 0; bottom: 0; width: 516px; height: 560px;
    background: linear-gradient(180deg, #cdd0d5 0%, #b7b4b1 35%, #4a6f9c 70%, #2b2d33 100%);
  }
  .clinic-mark {
    position: absolute; left: 540px; top: 160px; width: 390px;
    display: flex; align-items: center; gap: 18px;
  }
  .clinic-mark .square { width: 86px; height: 86px; background: var(--slate); flex: none; }
  .clinic-mark .name {
    font-family: var(--serif); font-weight: 600; color: var(--slate);
    font-size: 40px; line-height: 1.05; text-transform: uppercase;
  }

  .name-band {
    height: 219px; flex: none; background: var(--slate); color: var(--white);
    display: flex; flex-direction: column; align-items: center; justify-content: center;
    font-family: var(--serif);
  }
  .name-band h1 { font-size: 54px; font-weight: 600; letter-spacing: 1px; line-height: 1.1; }
  .name-band p { font-size: 32px; line-height: 1.2; margin-top: 4px; }

  .bio {
    height: 878px; flex: none; padding: 46px 50px 0 46px;
    font-family: var(--serif); color: var(--ink);
    font-size: 31.5px; line-height: 35px; text-align: justify;
  }
  .bio ul { list-style: none; margin-top: 32px; }
  .bio li { margin-bottom: 17px; }
  .bio li::before { content: "\2022\00a0"; }

  .quote-bar {
    height: 101px; flex: none; background: var(--magenta); color: var(--white);
    display: flex; align-items: center; justify-content: center;
    font-family: var(--serif); font-size: 34px;
  }

  .contacts {
    height: 220px; flex: none; background: var(--slate); color: var(--white);
    font-family: var(--sans); position: relative;
  }
  .clinic { position: absolute; top: 30px; }
  .clinic.little-rock { left: 50px; }
  .clinic.pine-bluff { left: 535px; top: 38px; }
  .clinic h2 { font-size: 29px; font-weight: 400; line-height: 1.15; }
  .clinic .assoc { font-size: 18px; line-height: 22px; }
  .clinic .line {
    display: flex; align-items: center; gap: 12px;
    font-size: 18.5px; margin-top: 12px;
  }
  .clinic .line svg { width: 17px; height: 17px; fill: var(--white); flex: none; }
  .clinic .line .gap { width: 20px; }
</style>
</head>
<body>
<main class="card">
  <header class="site-bar">WWW.CEDARLINEBLOOD.COM</header>

  <section class="hero">
    <div class="hero-backdrop" role="img" aria-label="Soft light office backdrop"></div>
    <div class="portrait" role="img" aria-label="Portrait photograph of Dr. Dun Harlow in dark suit, blue shirt and tie"></div>
    <div class="clinic-mark">
      <span class="square"></span>
      <span class="name">Cedarline<br>Blood Institute</span>
    </div>
  </section>

  <section class="name-band">
    <h1>DUN HARLOW, M.D.</h1>
    <p>Cedarline Blood Institute</p>
  </section>

  <section class="bio">
    <p>I completed my Hematology Oncology fellowship training at Lakeshore State University, Brookfield, MI. in 2006. Since then I have practiced privately, and I currently see patients at two office locations, Pine Bluff and Little Rock. In addition I have served as;</p>
    <ul>
      <li>Associate Chief of Internal Medicine at Pinecrest Regional Hospital (PRMC), from March 2016 - February 2018</li>
      <li>Chair of Quality and Peer Review Committee, PRMC, March 2016 - February 2018,</li>
      <li>Member of Credentials Committee, PRMC, March 2016 - February 2018.</li>
      <li>Regional Oncology Society of Arkansas, State Chapter President, March 2016 - February 2017.</li>
      <li>Regional Oncology Society - Director of Guest Lecture Series, March 2016 - February 2018</li>
      <li>Adjunct Assistant Clinical Professor. Internal Medicine residents, RMSU, 2006 - present.</li>
      <li>Volunteer attending physician at Riverbend Medical Sciences University community health clinic (Eastside clinic)</li>
    </ul>
  </section>

  <section class="quote-bar">" I appreciate the opportunity to serve you and your patients"</section>

  <footer class="contacts">
    <div class="clinic little-rock">
      <h2>Little Rock Clinic</h2>
      <p class="assoc">In association with<br>Mercy Hill Hospital</p>
      <p class="line">
        <svg viewBox="0 0 24 24" aria-hidden="true"><path d="M6.6 10.8a15.2 15.2 0 0 0 6.6 6.6l2.2-2.2c.3-.3.7-.4 1-.2 1.1.4 2.3.6 3.6.6.6 0 1 .4 1 1V20c0 .6-.4 1-1 1A17 17 0 0 1 3 4c0-.6.4-1 1-1h3.5c.6 0 1 .4 1 1 0 1.3.2 2.5.6 3.6.1.3 0 .7-.2 1z"/></svg>
        501-555-0174<span class="gap"></span>
        <svg viewBox="0 0 24 24" aria-hidden="true"><path d="M6 2h10l2 2v5H6zM3 10h18v8h-3v4H6v-4H3zm5 6v4h8v-4z"/></svg>
        501-555-0136
      </p>
      <p class="line">
        <svg viewBox="0 0 24 24" aria-hidden="true"><path d="M12 2a7 7 0 0 0-7 7c0 5 7 13 7 13s7-8 7-13a7 7 0 0 0-7-7zm0 9.5A2.5 2.5 0 1 1 12 6.5a2.5 2.5 0 0 1 0 5z"/></svg>
        420 S. Harbor Ave. Suite 210, 72205
      </p>
    </div>
    <div class="clinic pine-bluff">
      <h2>Pine Bluff Clinic</h2>
      <p class="assoc">In association with Pinecrest Regional<br>Memorial Hospital</p>
      <p class="line">
        <svg viewBox="0 0 24 24" aria-hidden="true"><path d="M6.6 10.8a15.2 15.2 0 0 0 6.6 6.6l2.2-2.2c.3-.3.7-.4 1-.2 1.1.4 2.3.6 3.6.6.6 0 1 .4 1 1V20c0 .6-.4 1-1 1A17 17 0 0 1 3 4c0-.6.4-1 1-1h3.5c.6 0 1 .4 1 1 0 1.3.2 2.5.6 3.6.1.3 0 .7-.2 1z"/></svg>
        870-555-0188<span class="gap"></span>
        <svg viewBox="0 0 24 24" aria-hidden="true"><path d="M6 2h10l2 2v5H6zM3 10h18v8h-3v4H6v-4H3zm5 6v4h8v-4z"/></svg>
        870-555-0148
      </p>
      <p class="line">
        <svg viewBox="0 0 24 24" aria-hidden="true"><path d="M12 2a7 7 0 0 0-7 7c0 5 7 13 7 13s7-8 7-13a7 7 0 0 0-7-7zm0 9.5A2.5 2.5 0 1 1 12 6.5a2.5 2.5 0 0 1 0 5z"/></svg>
        1870 S. Linden St. Pine Bluff 71603
      </p>
    </div>
  </footer>
</main>
</body>
</html>
```